Tavo Payments Business card refresh

Need a new design of our business card The info is not what is on these cards i sent this for a reference. I can email all the info over
Info would be Derek Whitfield Chief TAVO is the title. our new address is 47615 Birch Hollow Rd. Westlake Village Ca 91384 Cell number is 805-634-2917 Work number is 855-482-7309 ext 212 Derek@tavopayments.com is my email address
Target Market(s)
Merchant Services all businesses that take credit cards
Industry/Entity Type
Merchant Services / Credit Card processing
Contact Information for Business Card
Need a new design of our business card The info is not what is on these cards i sent this for a reference. I can email all the info over Info would be Derek Whitfield Chief TAVO is the title. our new address is 47615 Birch Hollow Rd. Westlake Village Ca 91384 Cell number is 805-634-2917 Work number is 855-482-7309 ext 212 Derek@tavopayments.com is my email address
Requirements
Must have
- My logo and colors from my brand guidelines
Nice to have
- i sent some designs just need a new refresh
Should not have
- nothing specific

```html
<!DOCTYPE html>
<html lang="en">
<head>
<meta charset="utf-8">
<title>Tavo Payments – Business Cards</title>
<link href="https://fonts.googleapis.com/css2?family=Montserrat:wght@400;500;700;800&display=swap" rel="stylesheet">
<style>
  :root {
    --bg-light: #e9e9e9;
    --bg-dark: #bdbdbd;
    --card-top: #4b494a;
    --card-bottom: #1e1c1d;
    --green: #8dc041;
    --white: #ffffff;
    --ink-soft: #f2f2f2;
  }
  * { box-sizing: border-box; margin: 0; padding: 0; }
  html, body { width: 1200px; height: 1200px; overflow: hidden; }
  body {
    background: linear-gradient(135deg, var(--bg-light), var(--bg-dark));
    font-family: "Montserrat", sans-serif;
    color: var(--white);
    position: relative;
  }
  .card {
    position: absolute;
    left: 120px;
    width: 960px;
    height: 548px;
    border-radius: 30px;
    overflow: hidden;
    background: linear-gradient(150deg, var(--card-top) 0%, #2c2a2b 45%, var(--card-bottom) 100%);
    box-shadow: 0 14px 30px rgba(0,0,0,0.35);
  }
  .card--services { top: 40px; }
  .card--contact { top: 612px; }

  .brand {
    position: absolute;
    left: 0; right: 0;
    top: 60px;
    display: flex;
    align-items: center;
    justify-content: center;
    gap: 14px;
    font-weight: 800;
    font-size: 54px;
    letter-spacing: 2px;
    color: var(--white);
  }
  .brand__mark { width: 26px; height: 26px; background: var(--green); }

  .service-list {
    position: absolute;
    list-style: none;
    font-size: 25px;
    font-weight: 500;
    line-height: 35px;
  }
  .service-list li::before {
    content: "•";
    color: var(--green);
    margin-right: 12px;
  }
  .service-list--left { left: 150px; top: 210px; }
  .service-list--right { left: 540px; top: 180px; }

  .tagline {
    position: absolute;
    left: 0; right: 0;
    top: 402px;
    text-align: center;
    font-weight: 800;
    font-size: 33px;
    color: var(--green);
    letter-spacing: 0.5px;
  }
  .referral {
    position: absolute;
    left: 0; right: 0;
    top: 452px;
    text-align: center;
    font-size: 24px;
    font-weight: 500;
  }

  .person {
    position: absolute;
    right: 500px;
    top: 196px;
    text-align: right;
  }
  .person__name { font-size: 44px; font-weight: 800; color: var(--green); }
  .person__title { font-size: 26px; font-weight: 500; margin-top: 4px; }
  .divider {
    position: absolute;
    left: 492px; top: 196px;
    width: 2px; height: 100px;
    background: var(--ink-soft);
  }
  .phones {
    position: absolute;
    left: 530px; top: 206px;
    list-style: none;
    font-size: 28px;
    font-weight: 500;
    line-height: 40px;
  }
  .phones__label { color: var(--green); }
  .address {
    position: absolute;
    left: 0; right: 0;
    top: 326px;
    text-align: center;
    font-size: 27px;
    font-weight: 500;
    color: var(--green);
  }
  .swoosh { position: absolute; left: 0; top: 0; width: 960px; height: 548px; }
  .email {
    position: absolute;
    right: 60px;
    bottom: 48px;
    font-size: 27px;
    font-weight: 500;
  }
</style>
</head>
<body>

  <section class="card card--services">
    <div class="brand"><span class="brand__mark"></span>TAVO PAYMENTS</div>
    <ul class="service-list service-list--left">
      <li>Credit Card Processing</li>
      <li>Check Guarantee</li>
      <li>Gift Cards</li>
      <li>Loyalty Cards</li>
      <li>ACH Deposits</li>
    </ul>
    <ul class="service-list service-list--right">
      <li>24/7 Customer Support</li>
      <li>Same Day Approvals</li>
      <li>ATM Sales</li>
      <li>ATM Placement</li>
      <li>Merchant Funding</li>
    </ul>
    <p class="tagline">BEST RATES, BEST SERVICE - GUARNTEED</p>
    <p class="referral">Ask about our “ Merchant Referral ” Program</p>
  </section>

  <section class="card card--contact">
    <svg class="swoosh" viewBox="0 0 960 548" aria-hidden="true">
      <path d="M0 548 L0 522 C 200 484, 420 432, 660 402 C 430 444, 230 502, 90 548 Z" fill="#f1f1f1"/>
      <path d="M40 548 C 260 500, 570 430, 960 400 L960 548 Z" fill="var(--green)"/>
    </svg>
    <div class="brand"><span class="brand__mark"></span>TAVO PAYMENTS</div>
    <div class="person">
      <p class="person__name">Derek Whitfield</p>
      <p class="person__title">Chief TAVO</p>
    </div>
    <div class="divider"></div>
    <ul class="phones">
      <li><span class="phones__label">C:</span> 805-634-2917</li>
      <li><span class="phones__label">O:</span> 855-482-7309 ext 212</li>
    </ul>
    <p class="address">47615 Birch Hollow Rd. Westlake Village Ca 91384</p>
    <p class="email">Derek@tavopayments.com</p>
  </section>

</body>
</html>
```